Faith Based Film Production Ecommerce Site Needed

We are a faith based film production company that offers coaching services as well as physical and digital products.

We have a Wordpress site on Hostwren. It currently, features a landing page (https://brightlampstudio.net/), however we now need a fully fleshed out interactive website that will feature short videos/trailers as well the ability for customers to make online purchases.

The updated site will feature 5 tabs - Take 1, Take 2, Take 3, BTS and Contact. This toolbar/menu should remain fixed/stable while visitors navigate the different tabs/pages, as shown here - https://pelmarokane.com/ (note this site is JUST a reference for its unmoving menu/toolbar in the top right corner of the page).

The text for each tab and actual video content will be provided for potential candidates. Until then, please improvise.

There will be 5 short trailers/reels featured under the "Take 2" tab, that will be shown as thumbnails the same size found here - https://pelmarokane.com/see-pel-at-work/ (reference for thumbnail size only). The names of these trailers will be called, Lamp Summons, Lamp Flourish, Lamp Dawn, Lamp Hearth, and Lamp Courtship.

Lastly, when arriving onto the page, visitors will be greeted with a inaudible video loop, similar to the one found here - https://www.tq-moviehouse.com/ (Note - this is a reference simply to show inaudible video looping). The ACTUAL video to be used however can be found here - https://clipvaultr.net/manage/videos/473918265, beginning at the 15 second mark when the 3 people are entering the cinema and ending at the 28 second mark where the screen gradually fades to black. The video will then consistently re-loop.

Once again, more detail will be provided for the most interesting submissions and of course, official winner.

Should you have any questions until then, please do not hesitate to reach out.

```html
<!DOCTYPE html>
<html lang="en">
<head>
<meta charset="utf-8">
<title>Bright Lamp</title>
<link href="https://fonts.googleapis.com/css2?family=Poppins:wght@400;500;600;700&display=swap" rel="stylesheet">
<style>
:root{
  --ink:#222222;
  --white:#ffffff;
  --orange:#ff6600;
  --cream:#faf0e0;
  --mist:#f5f5f5;
  --night:#1b1e33;
  --footer:#232323;
  --line:#d6d6d6;
}
*{margin:0;padding:0;box-sizing:border-box}
html,body{width:1200px;height:2769px;overflow:hidden}
body{position:relative;font-family:'Poppins',sans-serif;color:var(--ink);background:var(--white)}
.abs{position:absolute}

/* hero */
.hero{left:0;top:0;width:1200px;height:670px;
  background:radial-gradient(ellipse at 45% 40%,#4a3a4a 0%,#2a2840 45%,#151828 100%)}
.nav{top:80px;display:flex;gap:32px;font-size:15px;font-weight:600;color:var(--white);letter-spacing:.3px}
.nav-left{left:194px}
.nav-right{left:793px;gap:36px}
.brand{left:500px;width:200px;text-align:center;color:var(--white);font-weight:700;font-size:22px;letter-spacing:1px}
.brand-mark{display:block;width:36px;height:36px;margin:0 auto 12px;border:3px solid var(--white)}
.hero-brand{top:40px}
.hero-title{left:0;width:1200px;top:272px;text-align:center;color:var(--white);font-size:84px;font-weight:700;line-height:1}
.hero-text{left:0;width:1200px;top:368px;text-align:center;color:var(--white);font-size:22.5px;line-height:33px}

/* about */
.about-band{left:0;top:670px;width:497px;height:583px;background:var(--cream)}
.about-photo{left:75px;top:744px;width:512px;height:436px;background:linear-gradient(160deg,#a9b1b0 0%,#5a6256 45%,#3c4a2e 75%,#262626 100%)}
.about-title{left:622px;top:752px;font-size:54px;font-weight:700;line-height:57px}
.about-text{left:615px;top:888px;width:520px;font-size:15.5px;line-height:32.3px}
.btn{background:var(--orange);color:var(--white);font-weight:700;display:flex;align-items:center;justify-content:center}
.about-btn{left:615px;top:1107px;width:179px;height:55px;font-size:19px}

/* reels */
.reels{left:0;top:1310px;width:1200px;height:537px;background:var(--mist)}
.reels-title{left:0;width:1200px;top:1374px;text-align:center;font-size:54px;font-weight:700;line-height:64px}
.reel{top:1472px;width:328px}
.reel-thumb{height:248px;border-radius:8px;position:relative}
.reel-play{position:absolute;left:138px;top:98px}
.reel-name{margin-top:16px;text-align:center;font-size:20px;font-weight:600}
.thumb-a{background:linear-gradient(135deg,#3a3a3a,#1c1c1c 60%,#5a4a3a)}
.thumb-b{background:linear-gradient(180deg,#8a96a8,#d8dde4 50%,#eef0f3)}
.thumb-c{background:linear-gradient(135deg,#3d4a3a,#a8b4c8 55%,#e6d8c8)}
.arrow{top:1600px}

/* contact */
.contact-band{left:704px;top:1907px;width:496px;height:583px;background:var(--cream)}
.contact-photo{left:614px;top:1982px;width:512px;height:435px;background:linear-gradient(135deg,#6a5a3a 0%,#2a2a2a 40%,#3a2a2a 70%,#7a4a4a 100%)}
.contact-title{left:75px;top:1985px;font-size:54px;font-weight:700;line-height:60px}
.field{border:1px solid var(--line);background:var(--white);font-size:15.5px;color:#444;padding:0 18px;display:flex;align-items:center}
.field-msg{align-items:flex-start;padding-top:18px}
.submit{left:75px;top:2348px;width:241px;height:53px;font-size:23px}

/* footer */
.footer{left:0;top:2548px;width:1200px;height:221px;background:var(--footer)}
.foot-links{left:75px;top:2607px;display:flex;gap:30px;color:var(--white);font-size:16px;font-weight:600}
.foot-copy{left:75px;top:2657px;color:var(--white);font-size:14px;line-height:26px}
.foot-brand{top:2604px}
.follow{left:912px;top:2620px;color:var(--white);font-size:16px;font-weight:600}
.socials{left:912px;top:2662px;display:flex;gap:29px}
.social{width:30px;height:30px;background:var(--white);border-radius:4px}
</style>
</head>
<body>

<div class="abs hero" role="img" aria-label="Moviegoers eating popcorn in a darkened cinema"></div>
<nav class="abs nav nav-left"><span>HOME</span><span>TAKE 1</span><span>TAKE 2</span></nav>
<div class="abs brand hero-brand"><span class="brand-mark"></span>BRIGHT LAMP</div>
<nav class="abs nav nav-right"><span>TAKE 3</span><span>BTS</span><span>CONTACT</span></nav>
<h1 class="abs hero-title">Bright Lamp</h1>
<p class="abs hero-text">We are a faith based film production company that offers coaching<br>services as well as physical and digital products.</p>

<div class="abs about-band"></div>
<div class="abs about-photo" role="img" aria-label="Film crew member standing on an outdoor set beside monitors"></div>
<h2 class="abs about-title">About<br>Bright Lamp</h2>
<p class="abs about-text">Nemo enim ipsam voluptatem quia voluptas sit aspernatur aut odit aut fugit, sed quia consequuntur magni dolores eos qui ratione voluptatem sequi nesciunt. Neque porro quisquam est, qui dolorem ipsum quia dolor sit amet, consectetur, adipisci velit, sed quia non numquam eius modi tempora incidunt ut labore et dolore magnam aliquam quaerat voluptatem.</p>
<div class="abs btn about-btn">Read More</div>

<div class="abs reels"></div>
<h2 class="abs reels-title">Take 2</h2>
<svg class="abs arrow" style="left:38px" width="24" height="34" viewBox="0 0 24 34"><path d="M18 3 4 17l14 14" fill="none" stroke="#222" stroke-width="2.5"/></svg>
<svg class="abs arrow" style="left:1138px" width="24" height="34" viewBox="0 0 24 34"><path d="M6 3l14 14L6 31" fill="none" stroke="#222" stroke-width="2.5"/></svg>

<div class="abs reel" style="left:75px">
  <div class="reel-thumb thumb-a" role="img" aria-label="Editor working at a computer workstation">
    <svg class="reel-play" width="54" height="54" viewBox="0 0 54 54"><circle cx="27" cy="27" r="24" fill="none" stroke="#fff" stroke-width="4"/><path d="M21 15l17 12-17 12z" fill="#fff"/></svg>
  </div>
  <div class="reel-name">Lamp Summons</div>
</div>
<div class="abs reel" style="left:437px">
  <div class="reel-thumb thumb-b" role="img" aria-label="Skier descending a snowy mountain slope">
    <svg class="reel-play" width="54" height="54" viewBox="0 0 54 54"><circle cx="27" cy="27" r="24" fill="none" stroke="#fff" stroke-width="4"/><path d="M21 15l17 12-17 12z" fill="#fff"/></svg>
  </div>
  <div class="reel-name">Lamp Flourish</div>
</div>
<div class="abs reel" style="left:799px">
  <div class="reel-thumb thumb-c" role="img" aria-label="Woman outdoors among trees lifting her face to the sky">
    <svg class="reel-play" width="54" height="54" viewBox="0 0 54 54"><circle cx="27" cy="27" r="24" fill="none" stroke="#fff" stroke-width="4"/><path d="M21 15l17 12-17 12z" fill="#fff"/></svg>
  </div>
  <div class="reel-name">Lamp Dawn</div>
</div>

<div class="abs contact-band"></div>
<div class="abs contact-photo" role="img" aria-label="Camera operators filming on set with a cinema camera"></div>
<h2 class="abs contact-title">Contact Us</h2>
<div class="abs field" style="left:75px;top:2080px;width:241px;height:53px">Name</div>
<div class="abs field" style="left:329px;top:2080px;width:242px;height:53px">Email Address</div>
<div class="abs field" style="left:75px;top:2147px;width:241px;height:53px">Phone No</div>
<div class="abs field" style="left:329px;top:2147px;width:242px;height:53px">Subject</div>
<div class="abs field field-msg" style="left:75px;top:2213px;width:496px;height:120px">Message</div>
<div class="abs btn submit">Submit</div>

<footer class="abs footer"></footer>
<nav class="abs foot-links"><span>Take 1</span><span>Take 2</span><span>Take 3</span><span>BTS</span><span>Contact</span></nav>
<p class="abs foot-copy">Copyright © 2023 Company Name<br>All rights reserved</p>
<div class="abs brand foot-brand"><span class="brand-mark"></span>BRIGHT LAMP</div>
<div class="abs follow">Follow Us</div>
<div class="abs socials"><span class="social"></span><span class="social"></span><span class="social"></span><span class="social"></span></div>

</body>
</html>
```